Design Startseite Kanzlei-Homepage
Zielgruppe
Wir sind eine Rechtsanwaltskanzlei in Kempten (Allgäu) und regional sowie überregional in verschiedenen Rechtsgebieten tätig. Unsere Zielgruppe sind sowohl private als auch gewerbliche Mandanten.
Aufgabenstellung
Die bestehende Gestaltung wirkt derzeit aus unserer Sicht überholt. Insbesondere soll das bislang dominierende Rot vollständig entfallen.
Stattdessen stellen wir uns ein modernes, hochwertiges Erscheinungsbild vor, primär in dunklen Farbtönen (Anthrazit/Schwarz) kombiniert mit Beige- bzw. warmen Naturtönen. Ziel ist eine klare visuelle Anlehnung an unsere Kanzleiräumlichkeiten (siehe Fotos).
Die Webseite soll insgesamt moderner, klarer und visuell anspruchsvoller wirken, ohne an Seriosität und Zugänglichkeit einzubüßen. Die Balance zwischen hochwertigem Erscheinungsbild und mandantenorientierter Nutzerführung steht für uns im Vordergrund.

```html
<!DOCTYPE html>
<html lang="de">
<head>
<meta charset="utf-8">
<title>Kanzlei am Rathaus – Rechtsanwälte in Kempten</title>
<link href="https://fonts.googleapis.com/css2?family=Cinzel:wght@400;500&family=Fira+Sans:wght@400;500;600;700&display=swap" rel="stylesheet">
<style>
:root{
  --brown:#8b6e4d;
  --brown-dark:#6f5439;
  --heading:#7e6142;
  --anthracite:#333333;
  --anthracite-deep:#2b2b2b;
  --text:#3a3a3a;
  --light:#f6f5f3;
  --field:#f1f0ee;
  --white:#ffffff;
}
*{box-sizing:border-box;margin:0;padding:0}
html,body{width:1200px;height:3265px;overflow:hidden}
body{position:relative;font-family:"Fira Sans",sans-serif;color:var(--text);background:var(--white);font-size:9px;line-height:1.55}
.abs{position:absolute}
.serif{font-family:"Cinzel",serif;font-weight:400}

/* top bar + nav */
.topbar{left:0;top:0;width:1200px;height:16px;background:var(--brown);color:var(--white);font-size:7px;line-height:16px}
.topbar span{position:absolute;display:flex;align-items:center;gap:4px}
.nav{left:0;top:16px;width:1200px;height:52px;background:var(--anthracite)}
.wordmark{font-family:"Cinzel",serif;font-weight:400;color:var(--white);white-space:nowrap;letter-spacing:.5px}
.nav-wordmark{left:215px;top:15px;font-size:17px;line-height:22px}
.menu a{position:absolute;top:0;height:52px;line-height:52px;color:var(--white);font-size:11.5px;text-decoration:none;text-align:center}
.menu a.active{background:var(--brown);width:77px}

/* hero */
.hero{left:0;top:68px;width:1200px;height:434px;background:linear-gradient(120deg,#7a5d3e 0%,#a78259 30%,#6a6460 55%,#3a3b3d 75%,#9a9fa3 100%)}
.hero-title{left:109px;top:308px;width:435px;height:66px;background:rgba(40,36,32,.78);color:var(--white);font-size:19px;line-height:28px;padding:5px 12px;letter-spacing:.4px}

/* split sections */
.photo-team{left:570px;top:452px;width:630px;height:377px;background:linear-gradient(180deg,#d8d6d2 0%,#8c8a88 45%,#aaa8a4 100%)}
.photo-meeting{left:0;top:829px;width:570px;height:378px;background:linear-gradient(110deg,#b8a49b 0%,#3f3a38 45%,#c9c3b8 70%,#2f3b3f 100%)}
.icon-box{width:55px;height:56px;background:var(--brown);display:flex;align-items:center;justify-content:center}
.label{font-family:"Cinzel",serif;color:var(--brown);font-size:8px;letter-spacing:.6px;text-transform:uppercase}
.bar-heading{border-left:2px solid var(--brown);padding-left:11px;font-family:"Cinzel",serif;font-weight:400;color:var(--heading);font-size:16px;line-height:20px;letter-spacing:.3px}
.body-text{font-size:7.6px;line-height:1.45;color:#333}
.body-text p+p{margin-top:8px}
.btn{background:var(--brown);color:var(--white);font-size:8px;font-weight:600;text-align:center;display:block}
.sep{left:0;top:1207px;width:1200px;height:1px;background:#dcdcdc}

/* practice areas */
.section-title{display:flex;align-items:center;gap:7px;font-family:"Cinzel",serif;font-weight:400;color:var(--heading);font-size:16px;letter-spacing:.4px}
.section-title i{width:14px;height:14px;background:var(--brown);display:inline-block}
.card{width:222px;height:260px;background:var(--anthracite)}
.card .img{height:126px}
.card .head{display:flex;align-items:center;height:36px;position:relative}
.card .head .ic{width:32px;height:32px;background:var(--brown);display:flex;align-items:center;justify-content:center;position:absolute;left:0;top:-14px}
.card h3{font-family:"Cinzel",serif;font-weight:400;color:var(--white);font-size:15px;letter-spacing:.3px;margin-left:48px;margin-top:4px}
.card p{color:#e6e6e6;font-size:8px;line-height:1.7;padding:2px 17px 0 17px}

/* video */
.video-intro{left:0;top:1908px;width:551px;height:381px;background:var(--light)}
.video-img{left:551px;top:1908px;width:649px;height:381px;background:radial-gradient(circle at 45% 40%,#c7a569 0%,#7a5530 45%,#3c2c20 100%)}
.play{left:840px;top:2072px;width:46px;height:46px;border-radius:50%;background:rgba(60,45,35,.55);display:flex;align-items:center;justify-content:center}

/* reviews */
.reviews{left:0;top:2304px;width:1200px;height:262px;background:linear-gradient(180deg,#3d3028 0%,#5b4636 50%,#3f3128 100%)}
.reviews h2{position:absolute;top:98px;width:1200px;text-align:center;color:var(--white);font-family:"Cinzel",serif;font-weight:400;font-size:21px;letter-spacing:.8px}
.reviews p{position:absolute;left:310px;top:144px;width:580px;text-align:center;color:#eee;font-size:7.5px;line-height:1.45}
.reviewer{position:absolute;left:523px;top:196px;width:154px;display:flex;align-items:center;gap:10px;color:var(--white);font-size:8px;font-weight:600;white-space:nowrap}
.reviewer i{flex:1;height:1px;background:rgba(255,255,255,.7)}

/* contact */
.map{left:0;top:2585px;width:551px;height:408px;background:linear-gradient(135deg,#e9e9e9 0%,#dadada 50%,#eeeeee 100%)}
.field{background:var(--field);font-size:8px;color:#555;padding:0 9px;display:flex;align-items:center}
.field.area{align-items:flex-start;padding-top:9px}

/* footer */
.footer{left:0;top:3015px;width:1200px;height:250px;background:var(--anthracite)}
.footer .col-title{font-family:"Cinzel",serif;color:var(--white);font-size:8px;letter-spacing:.5px}
.footer ul{list-style:none}
.footer li{color:var(--white);font-size:7px;height:15.5px;line-height:13px;border-bottom:1px solid #555;width:max-content;min-width:42px}
.footer .contact-line{display:flex;align-items:flex-start;gap:7px;color:var(--white);font-size:7px;line-height:1.5}
.social{width:16px;height:16px;background:var(--brown)}
.phone-btn{display:flex;align-items:center;border:1px solid #666;height:24px}
.phone-btn span{color:var(--white);font-size:8.5px;padding:0 10px}
.phone-btn .ic{width:24px;height:24px;background:var(--brown);display:flex;align-items:center;justify-content:center}
.copyright{color:#ddd;font-size:5.5px;letter-spacing:.3px;font-family:"Cinzel",serif}
</style>
</head>
<body>

<div class="abs topbar">
  <span style="left:215px"><svg width="7" height="6" viewBox="0 0 7 6"><rect x=".5" y=".5" width="6" height="5" fill="none" stroke="#fff" stroke-width=".8"/><path d="M.5 .5L3.5 3 6.5 .5" fill="none" stroke="#fff" stroke-width=".8"/></svg>info@kanzlei-am-rathaus.de</span>
  <span style="left:330px"><svg width="6" height="6" viewBox="0 0 10 10"><path d="M2 0L4 3 3 4C4 6 5 7 6 7L7 6 10 8 8 10C4 10 0 6 0 2Z" fill="#fff"/></svg>0831 400 217 50</span>
</div>

<header class="abs nav">
  <div class="abs wordmark nav-wordmark">Kanzlei am Rathaus</div>
  <nav class="menu">
    <a class="active" href="#" style="left:553px">Startseite</a>
    <a href="#" style="left:647px">Rechtsgebiete</a>
    <a href="#" style="left:755px">Kanzlei</a>
    <a href="#" style="left:823px">Kontakt</a>
  </nav>
</header>

<section class="abs hero" role="img" aria-label="Foto des Empfangsbereichs der Kanzlei mit Holzvertäfelung und Empfangstresen"></section>
<h1 class="abs hero-title serif">RECHTSANWÄLTE UND FACHANWÄLTE<br>IN KEMPTEN: KANZLEI AM RATHAUS</h1>

<div class="abs photo-team" role="img" aria-label="Gruppenfoto des Kanzleiteams auf einem gepflasterten Platz"></div>
<div class="abs icon-box" style="left:515px;top:501px">
  <svg width="26" height="24" viewBox="0 0 26 24" fill="none" stroke="#fff" stroke-width="1.3"><path d="M2 8L13 2 24 8Z"/><path d="M5 10v9M10 10v9M16 10v9M21 10v9M2 21h22"/></svg>
</div>
<div class="abs label" style="left:106px;top:545px">Unser Anwaltsteam</div>
<h2 class="abs bar-heading" style="left:106px;top:569px;width:360px">RECHTSANWÄLTE UND FACHANWÄLTE<br>IN KEMPTEN: KANZLEI AM RATHAUS</h2>
<div class="abs body-text" style="left:106px;top:622px;width:320px">
  <p>Die Mitglieder unseres Anwaltsteams – jeweils ergänzt um ein ansprechend eingerichtetes und funktional ausgestattetes Sekretariat – spezialisieren sich in unterschiedliche Fachrichtungen, sodass für Sie eine große Bandbreite in der mandantenorientierten Rechtsberatung sichergestellt ist. Das gilt insbesondere für unsere Schwerpunkte im Verkehrsrecht und Strafrecht sowie im Arbeitsrecht, Erbrecht, Mietrecht, Baurecht und Familienrecht.</p>
  <p>Auf die Mandatierung externer Anwälte kann durch die thematische Vielfalt und Spezialisierung unserer Juristen in den meisten Fällen verzichtet werden. Gleichzeitig gewährleistet unser engagiertes Kanzleiteam eine rechtliche Unterstützung ganz nach Ihren individuellen Interessen, stets auf dem neuesten Stand von Rechtsprechung und Praxis.</p>
</div>
<a class="abs btn" style="left:106px;top:757px;width:130px;height:17px;line-height:17px">Infos und Terminvereinbarung</a>

<div class="abs photo-meeting" role="img" aria-label="Foto eines Beratungsgesprächs mit drei Personen am Besprechungstisch"></div>
<div class="abs icon-box" style="left:570px;top:829px">
  <svg width="24" height="24" viewBox="0 0 24 24" fill="none" stroke="#fff" stroke-width="1.3"><path d="M4 20L20 4M8 4l12 12M4 8l4-4M16 20l4-4"/></svg>
</div>
<div class="abs label" style="left:702px;top:926px">Lorem Ipsum</div>
<h2 class="abs bar-heading" style="left:702px;top:950px;width:360px">NULPA QUUNT PARCIDENDION<br>RECTUS UT LAT QUODIPIS SOLESTI</h2>
<div class="abs body-text" style="left:703px;top:1006px;width:318px">
  <p>Nost, que vid quam eatur?<br>Nulpa quunt parcidendion rectus ut lat quodipis solesti derum sit endunt ditatur reped magnatum el ipicatur aborit eium abor aut molesto berum la pore, ut est occusanis alitaquas abo. Unt qui venti re vel milit imod quis ma volorunt ea alicae.</p>
  <p>Sit quodis dendebis moluptam quam nos quodis eum dolorpos quunt et hil ipsae niendi nonsed es ut quossitin pla necta consequi voluptaquat eturis assitia spedicit at aut doloris dia sandit que sin eos aligeni mporem faceper ehenden imenitatur? Lacerunt andisitio. Nam as quatur, iumque ne velessinciis dicisti blaborum excepel id modit exera volupta volupta tiorem acculpa quam, illtect ibusam, non rest offic to bea eum nihil exerfer speres mod eossum quiasped.</p>
</div>
<a class="abs btn" style="left:703px;top:1138px;width:65px;height:17px;line-height:17px">Lorem Ipsum</a>
<div class="abs sep"></div>

<h2 class="abs section-title" style="left:216px;top:1261px"><i></i>UNSERE RECHTSGEBIETE</h2>

<article class="abs card" style="left:216px;top:1303px">
  <div class="img" role="img" aria-label="Foto zweier Kinder, die nachdenklich auf einem Tisch liegen" style="background:linear-gradient(90deg,#c69a72,#e5d2bb,#b98c63)"></div>
  <div class="head"><div class="ic"><svg width="18" height="16" viewBox="0 0 18 16" fill="none" stroke="#fff" stroke-width="1.2"><circle cx="5" cy="4" r="2.5"/><circle cx="13" cy="4" r="2.5"/><path d="M1 15c0-4 2-6 4-6s4 2 4 6M9 15c0-4 2-6 4-6s4 2 4 6"/></svg></div><h3>FAMILIENRECHT</h3></div>
  <p>Lorem ipsum dolor sit amet, consectetur adipiscing elit, sed do eiusmod tempor incididunt ut labore et dolore magna aliqua. Quis ipsum suspendisse ultrices gravida. Risus commodo viverra maecenas accumsan lacus vel facilisis.</p>
</article>
<article class="abs card" style="left:493px;top:1303px">
  <div class="img" role="img" aria-label="Foto einer Hand, die einen Vertrag unterschreibt" style="background:linear-gradient(160deg,#9a8a7c,#efeeec 55%,#cfcac2)"></div>
  <div class="head"><div class="ic"><svg width="18" height="15" viewBox="0 0 18 15" fill="none" stroke="#fff" stroke-width="1.2"><rect x="1" y="4" width="16" height="10"/><path d="M6 4V1h6v3M1 8h16"/></svg></div><h3>ARBEITSRECHT</h3></div>
  <p>Lorem ipsum dolor sit amet, consectetur adipiscing elit, sed do eiusmod tempor incididunt ut labore et dolore magna aliqua. Quis ipsum suspendisse ultrices gravida. Risus commodo viverra maecenas accumsan lacus vel facilisis.</p>
</article>
<article class="abs card" style="left:770px;top:1303px">
  <div class="img" role="img" aria-label="Foto von Autos auf einer Straße" style="background:linear-gradient(110deg,#4c4e50,#8f9194 50%,#5f6163)"></div>
  <div class="head"><div class="ic"><svg width="18" height="14" viewBox="0 0 18 14" fill="none" stroke="#fff" stroke-width="1.2"><path d="M1 9l2-5h12l2 5v3H1Z"/><circle cx="5" cy="12" r="1.5"/><circle cx="13" cy="12" r="1.5"/></svg></div><h3>VERKEHRSRECHT</h3></div>
  <p>Lorem ipsum dolor sit amet, consectetur adipiscing elit, sed do eiusmod tempor incididunt ut labore et dolore magna aliqua. Quis ipsum suspendisse ultrices gravida. Risus commodo viverra maecenas accumsan lacus vel facilisis.</p>
</article>

<article class="abs card" style="left:216px;top:1597px">
  <div class="img" role="img" aria-label="Foto einer Justitia-Statue mit Waage" style="background:linear-gradient(90deg,#f3f1ee,#8a6a45 50%,#efece8)"></div>
  <div class="head"><div class="ic"><svg width="18" height="16" viewBox="0 0 18 16" fill="none" stroke="#fff" stroke-width="1.2"><path d="M9 1v14M3 15h12M2 3h14M2 3l-1.5 5h3ZM16 3l-1.5 5h3Z"/></svg></div><h3>STRAFRECHT</h3></div>
  <p>Lorem ipsum dolor sit amet, consectetur adipiscing elit, sed do eiusmod tempor incididunt ut labore et dolore magna aliqua. Quis ipsum suspendisse ultrices gravida. Risus commodo viverra maecenas accumsan lacus vel facilisis.</p>
</article>
<article class="abs card" style="left:493px;top:1597px">
  <div class="img" role="img" aria-label="Foto eines Gesetzbuchs zum Erbrecht mit Richterhammer" style="background:linear-gradient(100deg,#2d4f86,#3d62a0 55%,#6b3a25)"></div>
  <div class="head"><div class="ic"><svg width="16" height="16" viewBox="0 0 16 16" fill="none" stroke="#fff" stroke-width="1.2"><circle cx="8" cy="3" r="2"/><circle cx="3" cy="11" r="2"/><circle cx="13" cy="11" r="2"/><path d="M8 5v3M3 9V8h10v1"/></svg></div><h3>ERBRECHT</h3></div>
  <p>Lorem ipsum dolor sit amet, consectetur adipiscing elit, sed do eiusmod tempor incididunt ut labore et dolore magna aliqua. Quis ipsum suspendisse ultrices gravida. Risus commodo viverra maecenas accumsan lacus vel facilisis.</p>
</article>
<article class="abs card" style="left:770px;top:1597px">
  <div class="img" role="img" aria-label="Foto eines gekündigten Mietvertrags mit Stempel" style="background:linear-gradient(120deg,#f1efec,#dcd6ce 60%,#8b5a3a)"></div>
  <div class="head"><div class="ic"><svg width="14" height="16" viewBox="0 0 14 16" fill="none" stroke="#fff" stroke-width="1.2"><rect x="1" y="1" width="12" height="14"/><path d="M4 5h6M4 8h6M4 11h4"/></svg></div><h3>MIETRECHT</h3></div>
  <p>Lorem ipsum dolor sit amet, consectetur adipiscing elit, sed do eiusmod tempor incididunt ut labore et dolore magna aliqua. Quis ipsum suspendisse ultrices gravida. Risus commodo viverra maecenas accumsan lacus vel facilisis.</p>
</article>

<section class="abs video-intro">
  <h2 class="abs serif" style="left:120px;top:114px;color:var(--heading);font-size:15.5px;letter-spacing:.4px">IMAGE-VIDEO DER KANZLEI</h2>
  <p class="abs body-text" style="left:117px;top:155px;width:312px">Sit quodis dendebis moluptam quam nos quodis eum dolorpos quunt et hil ipsae niendi nonsed es ut quossitin pla necta consequi voluptaquat eturis assitia spedicit at aut doloris dia sandit que sin eos aligeni mporem faceper ehenden imenitatur? Lacerunt andisitio. Nam as quatur, iumque ne velessinciis dicisti blaborum excepel id modit exera volupta volupta tiorem acculpa quam, illtect ibusam, non rest offic to bea eum nihil exerfer speres mod eossum quiasped.</p>
</section>
<div class="abs video-img" role="img" aria-label="Vorschaubild des Kanzlei-Videos: Hausmodell mit Richterhammer auf Holztisch"></div>
<div class="abs play"><svg width="18" height="20" viewBox="0 0 18 20" fill="none" stroke="#c9a467" stroke-width="1.5"><path d="M2 2l14 8-14 8Z"/></svg></div>

<section class="abs reviews" role="img" aria-label="Hintergrundfoto einer verzierten Gebäudefassade">
  <h2>BEWERTUNGEN</h2>
  <p>Sit quodis dendebis moluptam quam nos quodis eum dolorpos quunt et hil ipsae niendi nonsed es ut quossitin pla necta. Nmodit exera volupta volupta tiorem acculpa quam, illtect ibusam, non rest offic to bea eum nihil exerfer speres mod eossum quiasped. modit exera volupta volupta tiorem acculpa quam, illtect ibusam, non rest offic to bea eum nihil exerfer speres mod eossum quiasped.</p>
  <div class="reviewer"><i></i>Helga Brandner<i></i></div>
</section>

<div class="abs map" role="img" aria-label="Stadtplan von Kempten mit Markierung des Kanzleistandorts"></div>
<div class="abs icon-box" style="left:551px;top:2585px">
  <svg width="22" height="22" viewBox="0 0 22 22" fill="none" stroke="#fff" stroke-width="1.3"><path d="M18 12v8H2V4h8"/><path d="M8 14l1-4 9-9 3 3-9 9Z"/></svg>
</div>
<div class="abs label" style="left:640px;top:2600px;font-size:7.5px">Kontakt</div>
<h2 class="abs serif" style="left:640px;top:2625px;color:var(--heading);font-size:16px;letter-spacing:.3px">ONLINE-FORMULAR</h2>
<div class="abs field" style="left:638px;top:2698px;width:199px;height:36px">Name*</div>
<div class="abs field" style="left:843px;top:2698px;width:200px;height:36px">E-Mail</div>
<div class="abs field" style="left:638px;top:2751px;width:405px;height:35px">Telefon</div>
<div class="abs field" style="left:638px;top:2804px;width:405px;height:31px;justify-content:space-between">Betreff<svg width="8" height="5" viewBox="0 0 8 5"><path d="M1 1l3 3 3-3" fill="none" stroke="#888"/></svg></div>
<div class="abs field area" style="left:638px;top:2851px;width:405px;height:58px">Nachricht schreiben</div>
<a class="abs btn" style="left:640px;top:2943px;width:107px;height:22px;line-height:22px;font-size:9px">Absenden &gt;&gt;</a>

<footer class="abs footer">
  <div class="abs wordmark" style="left:319px;top:60px;font-size:11px;line-height:14px">Kanzlei am Rathaus</div>
  <div class="abs" style="left:322px;top:100px;display:flex;flex-direction:column;gap:7px">
    <div class="contact-line"><svg width="7" height="9" viewBox="0 0 7 9"><path d="M3.5 9S0 5 0 3.5a3.5 3.5 0 0 1 7 0C7 5 3.5 9 3.5 9Z" fill="#8b6e4d"/></svg><span>Kanzlei am Rathaus<br>Lindenweg 14, 87435 Kempten</span></div>
    <div class="contact-line"><svg width="7" height="7" viewBox="0 0 10 10"><path d="M2 0L4 3 3 4C4 6 5 7 6 7L7 6 10 8 8 10C4 10 0 6 0 2Z" fill="#8b6e4d"/></svg><span>0831 400 217 50</span></div>
    <div class="contact-line"><svg width="8" height="6" viewBox="0 0 8 6"><rect width="8" height="6" fill="#8b6e4d"/></svg><span>info@kanzlei-am-rathaus.de</span></div>
    <div class="contact-line" style="margin-top:3px"><span>Folge uns:</span></div>
    <div style="display:flex;gap:6px;margin-top:-3px"><div class="social"></div><div class="social"></div><div class="social"></div></div>
  </div>

  <div class="abs col-title" style="left:466px;top:66px">RECHTSGEBIETE</div>
  <ul class="abs" style="left:466px;top:100px">
    <li>Familienrecht</li><li>Arbeitsrecht</li><li>Verkehrsrecht</li><li>Strafrecht</li><li>Erbrecht</li><li>Mietrecht / Wohnungseigentumsrecht</li>
  </ul>

  <div class="abs col-title" style="left:633px;top:66px">LINKS</div>
  <ul class="abs" style="left:633px;top:100px">
    <li>Startseite</li><li>Rechtsgebiete</li><li>Kanzlei</li><li>Kontakt</li>
  </ul>

  <div class="abs col-title" style="left:758px;top:66px">BERATUNG</div>
  <div class="abs phone-btn" style="left:758px;top:97px">
    <div class="ic"><svg width="10" height="10" viewBox="0 0 10 10"><path d="M2 0L4 3 3 4C4 6 5 7 6 7L7 6 10 8 8 10C4 10 0 6 0 2Z" fill="#fff"/></svg></div>
    <span>+49 831 400 217 50</span>
  </div>
  <div class="abs copyright" style="left:758px;top:192px">COPYRIGHT © BRANDSTÄTTER MEDIENDESIGN 2026</div>
</footer>

</body>
</html>
```